Book Cover For Social Media Project

I am requiring a book cover for my upcoming book “Folding Waves Toward Harvests”

This book is for Network Marketers wanting to build their business on Social Media. Helping them get business from likes they receive on Chatterloom.

The book design needs to be clear that it is a business book that is all about social media is a fun, modern way.

Target Market(s)

Men and Women aged 18-65 wanting to make money from their social media accounts.

Industry/Entity Type

Business

Colors

Designer to choose colors to be used in the design.

Requirements
Must have
• Clear and obvious relationship to social media and business.
• The title “Folding Waves Toward Harvests”
• Author name “Dorian Halvette”
• Tag line “A Complete Handbook For Growing Your Direct Selling Venture Through Online Channels”
Nice to have
• Emojis that are used on Chatterloom.

```html
<!DOCTYPE html>
<html lang="en">
<head>
<meta charset="utf-8">
<title>Folding Waves Toward Harvests — Book Cover</title>
<link rel="stylesheet" href="https://fonts.googleapis.com/css2?family=Oswald:wght@200;300;400&display=swap">
<style>
  :root {
    --page-bg: #ececec;
    --cover-light: #f4f4f4;
    --cover-mid: #d6d6d6;
    --cover-edge: #bdbdbd;
    --ink: #1c1c1c;
    --ink-soft: #474747;
    --rule: #8a8a8a;
    --teal: #37b9ba;
    --teal-light: #6fd0cf;
    --teal-ring: #3aa8ac;
    --react-yellow: #f6c443;
    --react-red: #ee3f58;
    --react-blue: #5a7ec8;
    --photo-green: #9fb07a;
    --photo-grey: #c7c9cc;
    --photo-warm: #b08a6a;
    --white: #ffffff;
  }
  html, body {
    margin: 0;
    padding: 0;
    width: 1200px;
    height: 800px;
    overflow: hidden;
    background: var(--page-bg);
  }
  .canvas {
    position: relative;
    width: 1200px;
    height: 800px;
    display: flex;
    align-items: center;
    justify-content: center;
  }
  .book-cover {
    display: block;
    width: 480px;
    height: 720px;
    box-shadow: 0 10px 24px rgba(0,0,0,0.18);
    font-family: "Oswald", "Arial Narrow", sans-serif;
  }
  .title-small { font-weight: 300; font-size: 36px; fill: var(--ink); }
  .title-large { font-weight: 200; font-size: 150px; fill: var(--ink); }
  .title-mid   { font-weight: 200; font-size: 70px;  fill: var(--ink); }
  .tagline     { font-weight: 300; font-size: 21px;  fill: var(--ink-soft); }
  .author      { font-weight: 400; font-size: 46px;  fill: var(--white); letter-spacing: 1px; }
  .rule        { stroke: var(--rule); stroke-width: 1.2; }
  .photo-ring  { stroke: var(--teal-ring); stroke-width: 6; }
</style>
</head>
<body>
<main class="canvas">
  <svg class="book-cover" viewBox="0 0 493 740" role="img" aria-label="Book cover: Folding Waves Toward Harvests by Dorian Halvette">
    <defs>
      <radialGradient id="cover-bg" cx="50%" cy="40%" r="75%">
        <stop offset="0%" stop-color="var(--cover-light)"/>
        <stop offset="70%" stop-color="var(--cover-mid)"/>
        <stop offset="100%" stop-color="var(--cover-edge)"/>
      </radialGradient>
      <linearGradient id="band-fill" x1="0" x2="1" y1="0" y2="0">
        <stop offset="0%" stop-color="var(--teal)"/>
        <stop offset="55%" stop-color="var(--teal)"/>
        <stop offset="100%" stop-color="var(--teal-light)"/>
      </linearGradient>
      <linearGradient id="photo-left" x1="0" x2="1" y1="0" y2="1">
        <stop offset="0%" stop-color="var(--photo-green)"/>
        <stop offset="100%" stop-color="#e6e6e6"/>
      </linearGradient>
      <linearGradient id="photo-middle" x1="0" x2="0" y1="0" y2="1">
        <stop offset="0%" stop-color="#d4d6d8"/>
        <stop offset="100%" stop-color="var(--photo-grey)"/>
      </linearGradient>
      <linearGradient id="photo-right" x1="0" x2="1" y1="0" y2="1">
        <stop offset="0%" stop-color="var(--photo-warm)"/>
        <stop offset="100%" stop-color="#e2d3c2"/>
      </linearGradient>
    </defs>

    <rect class="cover-ground" width="493" height="740" fill="url(#cover-bg)"/>
    <g class="soft-circles" fill="var(--white)" opacity="0.22">
      <circle cx="380" cy="640" r="180"/>
      <circle cx="90" cy="720" r="140"/>
      <circle cx="290" cy="280" r="200" opacity="0.5"/>
    </g>

    <g class="title">
      <text class="title-small" x="57" y="68" textLength="104" lengthAdjust="spacingAndGlyphs">FOLDING</text>
      <text class="title-large" x="58" y="203" textLength="280" lengthAdjust="spacingAndGlyphs">WAVES</text>
      <text class="title-mid" x="142" y="271" textLength="296" lengthAdjust="spacingAndGlyphs">TOWARD HARVESTS</text>
    </g>

    <g class="photo-bubbles">
      <circle class="photo-ring" cx="385" cy="402" r="60" fill="url(#photo-right)" role="img" aria-label="Photo of a man smiling at a cafe table"/>
      <circle class="photo-ring" cx="135" cy="382" r="80" fill="url(#photo-left)" role="img" aria-label="Photo of a young man reading a tablet outdoors"/>
      <circle class="photo-ring" cx="272" cy="420" r="82" fill="url(#photo-middle)" role="img" aria-label="Photo of a woman sitting cross-legged with a laptop"/>
    </g>

    <g class="reactions">
      <circle cx="178" cy="450" r="16" fill="var(--react-yellow)" stroke="var(--white)" stroke-width="2"/>
      <circle cx="245" cy="476" r="18" fill="var(--react-red)" stroke="var(--white)" stroke-width="2"/>
      <circle cx="367" cy="432" r="15" fill="var(--react-blue)" stroke="var(--white)" stroke-width="2"/>
    </g>

    <g class="tagline-block">
      <line class="rule" x1="48" y1="542" x2="445" y2="542"/>
      <text class="tagline" x="246" y="573" text-anchor="middle" textLength="290" lengthAdjust="spacingAndGlyphs">A COMPLETE HANDBOOK FOR GROWING YOUR</text>
      <text class="tagline" x="246" y="598" text-anchor="middle" textLength="392" lengthAdjust="spacingAndGlyphs">DIRECT SELLING VENTURE THROUGH ONLINE CHANNELS</text>
      <line class="rule" x1="48" y1="607" x2="445" y2="607"/>
    </g>

    <g class="author-band">
      <rect x="0" y="652" width="493" height="68" fill="url(#band-fill)"/>
      <text class="author" x="246" y="705" text-anchor="middle" textLength="282" lengthAdjust="spacingAndGlyphs">DORIAN HALVETTE</text>
    </g>
  </svg>
</main>
</body>
</html>
```